Kestrel Lane flyer

Need a A6 size horizontal layout flyer. See attached example for ideas as well as some images I have which you can use. we are a hire car company that provides vehicles to clients who have recently been involved in car accidents and who's cars are currently getting fixed and so they lose the use of their own vehicle. see our website to keep flyer in line with website and for any further information kestrellane.com.au

Target Market(s)

people involved in not at fault car accidents

Industry/Entity Type

It Company

Requirements
Must have
• *ask people to let us know where they got our flyer from when they call us
• *call to action for people to call our phone number 1800 417 582
Should not have
• any mentioning that the vehicle is free

```html
<!DOCTYPE html>
<html lang="en">
<head>
<meta charset="utf-8">
<title>Kestrel Lane – Accident Replacement Cars</title>
<link href="https://fonts.googleapis.com/css2?family=Arimo:ital,wght@0,400;0,700;1,700&display=swap" rel="stylesheet">
<style>
  :root {
    --blue: #3a9bf5;
    --icon-blue: #3d9cf2;
    --green: #5cb820;
    --ink: #111111;
    --white: #ffffff;
    --disc: #e9e9e5;
    --disc-ring: #f4f4f1;
    --footer: #000000;
  }
  * { margin: 0; padding: 0; box-sizing: border-box; }
  html, body { width: 1200px; height: 851px; overflow: hidden; background: var(--white); }
  body { font-family: "Arimo", Arial, sans-serif; color: var(--ink); }
  .flyer { position: relative; width: 1200px; height: 851px; background: var(--white); overflow: hidden; }

  .hero { position: absolute; left: 0; top: 0; width: 1200px; height: 317px; }
  .hero svg { display: block; }

  .brand-panel { position: absolute; left: 0; top: 0; width: 1200px; height: 380px; pointer-events: none; }
  .brand-name {
    position: absolute; left: 315px; width: 516px; top: 312px;
    text-align: center; font-weight: 700; font-size: 38px; letter-spacing: 0.5px; color: var(--ink);
  }

  .steps { position: absolute; left: 0; top: 357px; width: 1200px; height: 220px; }
  .step {
    position: absolute; top: 6px; width: 226px; height: 226px; border-radius: 50%;
    background: var(--disc-ring);
    display: flex; align-items: center; justify-content: center;
  }
  .step-disc {
    width: 192px; height: 192px; border-radius: 50%; background: var(--disc);
    box-shadow: 0 2px 4px rgba(0,0,0,0.25);
    display: flex; flex-direction: column; align-items: center; justify-content: center; text-align: center;
  }
  .step-call { left: 203px; }
  .step-details { left: 494px; }
  .step-vehicle { left: 775px; }
  .call-label { font-size: 25px; font-weight: 700; line-height: 1.1; margin-top: 4px; }
  .call-number { font-size: 30px; font-weight: 700; line-height: 1.1; white-space: nowrap; }
  .call-free { font-size: 28px; font-weight: 700; font-style: italic; line-height: 1.05; }
  .details-label { font-size: 17px; font-weight: 700; line-height: 1.3; margin-top: 10px; letter-spacing: 0.3px; }
  .vehicle-label { font-size: 11.5px; font-weight: 700; line-height: 1.2; margin-top: 8px; }
  .arrow { position: absolute; top: 98px; }
  .arrow-one { left: 448px; }
  .arrow-two { left: 733px; }

  .benefits {
    position: absolute; left: 0; top: 577px; width: 1200px; height: 214px;
    background: var(--blue); color: var(--white);
    padding: 7px 36px 0 27px;
  }
  .benefit-list { list-style: none; }
  .benefit-list li {
    position: relative; padding-left: 19px; font-size: 16px; line-height: 21px; margin-bottom: 3px;
    letter-spacing: 0.25px;
  }
  .benefit-list li::before, .perk::before {
    content: ""; position: absolute; left: 0; top: 4px; width: 14px; height: 14px; border-radius: 50%;
    background: var(--footer);
  }
  .benefit-list li::after, .perk::after {
    content: ""; position: absolute; left: 4px; top: 8px; width: 4px; height: 4px;
    border-right: 2px solid var(--white); border-top: 2px solid var(--white); transform: rotate(45deg);
  }
  .highlight { font-weight: 700; font-style: italic; font-size: 20px; }
  .emphasis { font-weight: 700; font-style: italic; }
  .perks { position: absolute; top: 189px; left: 0; width: 1200px; height: 20px; }
  .perk { position: absolute; padding-left: 19px; font-size: 17px; font-weight: 700; line-height: 20px; }
  .perk-delivery { left: 355px; }
  .perk-models { left: 678px; top: 1px; }

  .footer {
    position: absolute; left: 0; top: 791px; width: 1200px; height: 60px; background: var(--footer);
    color: var(--white);
  }
  .footer-url {
    position: absolute; left: 0; top: 0; width: 1200px; text-align: center;
    font-size: 29px; font-weight: 700; font-style: italic; line-height: 60px; letter-spacing: 0.3px;
  }
  .footer-referral {
    position: absolute; right: 20px; top: 14px; width: 205px; text-align: right;
    font-size: 12.5px; font-weight: 700; line-height: 16px;
  }
</style>
</head>
<body>
<div class="flyer">

  <div class="hero">
    <svg width="1200" height="317" viewBox="0 0 1200 317">
      <defs>
        <linearGradient id="carTone" x1="0" y1="0" x2="1" y2="0">
          <stop offset="0" stop-color="#3a3a36"/>
          <stop offset="0.35" stop-color="#8d8d88"/>
          <stop offset="0.6" stop-color="#d9d9d7"/>
          <stop offset="1" stop-color="#b8b8b6"/>
        </linearGradient>
        <linearGradient id="cabinTone" x1="0" y1="0" x2="1" y2="1">
          <stop offset="0" stop-color="#6f6f72"/>
          <stop offset="0.45" stop-color="#d8cfc6"/>
          <stop offset="0.75" stop-color="#b9c8dc"/>
          <stop offset="1" stop-color="#c43a48"/>
        </linearGradient>
      </defs>
      <polygon points="0,0 670,0 620,317 0,317" fill="url(#carTone)" role="img" aria-label="Photo: front of a white late-model car parked on a country road"/>
      <polygon points="670,0 1200,0 1200,317 620,317" fill="url(#cabinTone)" role="img" aria-label="Photo: smiling couple driving a red replacement car"/>
    </svg>
  </div>

  <svg class="brand-panel" width="1200" height="380" viewBox="0 0 1200 380">
    <polygon points="315,227 831,227 781,367 405,367" fill="#ffffff"/>
    <polyline points="405,367 781,367" stroke="#bdbdbd" stroke-width="2" fill="none"/>
  </svg>
  <div class="brand-name">Kestrel Lane</div>

  <div class="steps">
    <div class="step step-call">
      <div class="step-disc">
        <svg width="34" height="46" viewBox="0 0 34 46" aria-hidden="true">
          <path d="M7 3 L13 1 L17 13 L12 16 Q14 26 22 33 L27 29 L33 38 L28 43 Q14 44 6 28 Q1 16 7 3 Z" fill="var(--icon-blue)"/>
        </svg>
        <div class="call-label">Call us on</div>
        <div class="call-number">1800 417 582</div>
        <div class="call-free">Free Call</div>
      </div>
    </div>
    <svg class="arrow arrow-one" width="35" height="38" viewBox="0 0 35 38" aria-hidden="true"><polygon points="0,0 35,19 0,38" fill="var(--green)"/></svg>
    <div class="step step-details">
      <div class="step-disc">
        <svg width="76" height="54" viewBox="0 0 76 54" aria-hidden="true">
          <path d="M44 14 Q76 12 75 30 Q74 42 62 44 L68 54 L52 45 Q34 46 33 32 Z" fill="var(--icon-blue)" stroke="#ffffff" stroke-width="2"/>
          <path d="M28 1 Q55 1 55 20 Q55 38 30 38 L10 47 L15 36 Q1 32 1 20 Q1 1 28 1 Z" fill="var(--icon-blue)" stroke="#ffffff" stroke-width="2"/>
        </svg>
        <div class="details-label">PROVIDE ACCIDENT<br>DETAILS</div>
      </div>
    </div>
    <svg class="arrow arrow-two" width="35" height="38" viewBox="0 0 35 38" aria-hidden="true"><polygon points="0,0 35,19 0,38" fill="var(--green)"/></svg>
    <div class="step step-vehicle">
      <div class="step-disc">
        <svg width="66" height="54" viewBox="0 0 66 54" aria-hidden="true">
          <path d="M14 4 Q15 1 19 1 L47 1 Q51 1 52 4 L57 20 Q65 22 65 30 L65 42 L1 42 L1 30 Q1 22 9 20 Z" fill="var(--icon-blue)"/>
          <path d="M17 6 L49 6 L52 19 L14 19 Z" fill="#ffffff"/>
          <rect x="5" y="42" width="10" height="11" rx="3" fill="var(--icon-blue)"/>
          <rect x="51" y="42" width="10" height="11" rx="3" fill="var(--icon-blue)"/>
          <circle cx="10" cy="30" r="4" fill="#ffffff"/>
          <circle cx="56" cy="30" r="4" fill="#ffffff"/>
          <rect x="20" y="26" width="26" height="3" fill="#ffffff"/>
          <rect x="20" y="32" width="26" height="3" fill="#ffffff"/>
        </svg>
        <div class="vehicle-label">YOU GET A REPLACEMENT<br>VEHICLE<br>WE TAKE CARE OF THE REST</div>
      </div>
    </div>
  </div>

  <div class="benefits">
    <ul class="benefit-list">
      <li>REPLACEMENT CAR: If you had an Accident <span class="highlight">Not At Fault</span> you are entitled to a Replacement Car The Replacement car will be delivered to your home, work or to your repairer</li>
      <li>WE OPERATE UNDER AUSTRALIAN LAW : If you find yourself saying it wasn’t my fault after an accident you were involved in then under Australian Law you are entitled to a replacement car. Insurance companies don’t readily advertise this given the fact that <span class="emphasis">they will be the ones paying for the costs incurred.</span></li>
      <li>A not at fault accident rental car would allow you to get a rental car without incurring the direct cost. The only cost you would be responsible for is putting petrol in it from time to time.</li>
      <li>The other person’s insurance company will pay for the rental car for as long as it takes for you to get your vehicle back.</li>
    </ul>
    <div class="perks">
      <span class="perk perk-delivery">Free Delivery</span>
      <span class="perk perk-models">Late Models/New Vehicles</span>
    </div>
  </div>

  <div class="footer">
    <div class="footer-url">www.kestrellane.com.au</div>
    <div class="footer-referral">When you call, please tell us where you got this flyer</div>
  </div>
</div>
</body>
</html>
```